Design Health Food E-Book for Small Business Using Provided Content

My business is looking for a designer to design and create an e-book PDF with recipes and images.

The required work will be:

Designing layout of e-book based on provided (below) e-book sample.

Adding supplied recipes and images into a PDF format

Iterating PDF until the work has reached satisfactory requirements

The outcome will be:

1 PDF document (roughly 10-15 pages) created using supplied recipes and images

This recipe e-book by Delia Marsh should serve as a strong piece of inspiration.

https://stirgrowthrive.shopvane.example/item/83k27dq4m190xz55t6b3c8e1

The full content of the e-book, including photos and copy, can be found here:

https://www.filecrate.example/sh/qrt517xk29w304b/BBDkunhwUPoeTvMzq8ErTXf4Gb?dl=0

Please arrange for a skype conversation if further clarification of e-book output and/or design are necessary.

Email: tobyr839@postmix.example

Industry/Entity Type

Health And Wellness

Font styles to use
Other font styles liked:
• Designer Choice

Requirements
Must have
• Book-like appearance (as in actually looks like a recipe book as opposed to a flyer, photo collection etc.
• Flawless page-linking (from contents page and to external sources) and no errors in text (unless we put a typo in!)
• Cute extra graphics (as per supplied Delia Marsh book)
Nice to have
• Designer interested in health food
• Experience in e-book design
Should not have
• Typos
• Errors in text linking

```html
<!DOCTYPE html>
<html lang="en">
<head>
<meta charset="utf-8">
<title>About Leafwise Tales</title>
<link rel="stylesheet" href="https://fonts.googleapis.com/css2?family=Carlito:ital@0;1&family=Parisienne&family=Tinos&display=swap">
<style>
  :root {
    --page-bg: #525669;
    --accent-peach: #e9cbbb;
    --body-text: #ffffff;
  }
  html, body {
    margin: 0;
    padding: 0;
    overflow: hidden;
    background: var(--page-bg);
  }
  .page {
    position: relative;
    width: 848px;
    height: 1200px;
    overflow: hidden;
    background: var(--page-bg);
    color: var(--body-text);
    font-family: "Carlito", "Calibri", sans-serif;
  }
  .corner-ornament {
    position: absolute;
    width: 168px;
    height: 165px;
  }
  .corner-ornament--top-left { top: 0; left: 0; background: radial-gradient(circle at 20% 20%, rgba(233,203,187,0.22), rgba(233,203,187,0) 70%); }
  .corner-ornament--top-right { top: 0; right: 0; background: radial-gradient(circle at 80% 20%, rgba(233,203,187,0.22), rgba(233,203,187,0) 70%); }
  .corner-ornament--bottom-left { bottom: 0; left: 0; background: radial-gradient(circle at 20% 80%, rgba(233,203,187,0.22), rgba(233,203,187,0) 70%); }
  .corner-ornament--bottom-right { bottom: 0; right: 0; background: radial-gradient(circle at 80% 80%, rgba(233,203,187,0.22), rgba(233,203,187,0) 70%); }

  .page-title {
    position: absolute;
    top: 118px;
    left: 0;
    width: 100%;
    margin: 0;
    text-align: center;
    font-family: "Parisienne", cursive;
    font-weight: 400;
    font-size: 58px;
    line-height: 76px;
    color: var(--accent-peach);
  }
  .intro {
    position: absolute;
    top: 239px;
    left: 60px;
    width: 728px;
    text-align: center;
    font-size: 17.6px;
    line-height: 24px;
  }
  .intro p { margin: 0 0 24px; }
  .intro .tagline {
    font-style: italic;
    font-size: 19px;
    margin-top: 26px;
  }
  .author-heading {
    position: absolute;
    top: 711px;
    left: 69px;
    margin: 0;
    font-family: "Tinos", "Times New Roman", serif;
    font-weight: 400;
    font-size: 26px;
    line-height: 34px;
    color: var(--accent-peach);
  }
  .author-bio {
    position: absolute;
    top: 781px;
    left: 66px;
    width: 716px;
    text-align: center;
    font-size: 17.6px;
    line-height: 34px;
  }
  .author-bio p {
    margin: 0 0 35px;
    text-indent: 26px;
  }
</style>
</head>
<body>
<main class="page">
  <div class="corner-ornament corner-ornament--top-left" role="img" aria-label="Line-drawn berries and leaves ornament"></div>
  <div class="corner-ornament corner-ornament--top-right" role="img" aria-label="Line-drawn berries and leaves ornament"></div>
  <div class="corner-ornament corner-ornament--bottom-left" role="img" aria-label="Line-drawn berries and leaves ornament"></div>
  <div class="corner-ornament corner-ornament--bottom-right" role="img" aria-label="Line-drawn berries and leaves ornament"></div>

  <h1 class="page-title">About Leafwise Tales</h1>

  <section class="intro">
    <p>The world has become enveloped by the fast-paced.</p>
    <p>Fast cars, fast internet, fast fixes and, of course, fast food.</p>
    <p>Cooking helps us slow down and enjoy the world, although we've been<br>convinced otherwise.</p>
    <p>From 10-minute recipes to just about anything that will get in your mouth ASAP, people are being driven away from the kitchen. We are growing increasingly disconnected from our food, particularly regarding how it is made and where it comes from.</p>
    <p>Leafwise’s plant-based recipes are designed for people who love to cook or who want to learn to use cooking as a creative outlet. 10-minute recipes are so boring! Get back in the kitchen and do something interesting. Don't fear the saucepan!</p>
    <p class="tagline">Be Leafwise!</p>
  </section>

  <h2 class="author-heading">About the author:</h2>

  <section class="author-bio">
    <p>Marisol Keane is a beach-loving, avocado obsessed, nutrition nerd. She has struggled for most of her life with chronic health problems, food allergies and digestive issues. The link between diet and health was so fascinating to her she decided to study Nutritional and Dietetic Medicine.</p>
    <p>Marisol founded Leafwise Tales to help people find joy in cooking again, get back in the kitchen and spend more time doing what they love.</p>
  </section>
</main>
</body>
</html>
```